Van Signage Wrapping

Hi there, my name is Wade; I have a business called "Vorplex" servicing the Electrical, Security & AV (audio visual) industry. I currently have 2 X Vans working in Australia; I am looking to design a the graphics & lay out for the 2 X vans to be identical wrapped.
Should you wish to see the Van appearance (silver)
http://www.morvane.com.au/cars/kelsovan/colours
http://www.morvane.com.au/cars/kelsovan/home

Dimensions of the side panels are:
from the revision mirror to the tail 3.6meters
from the bottom if plastic to the top 1.35meters

Some of the words that describe our services are:
Commercial, Domestic, Automation, Networking, Data, Access Control, Alarms, CCTV, Audio Visual, Surround Sound, Home Cinema.
Allot of our work is taking these various technologies & linking them together for the user
Updates

Hi there, I have added a couple of thoughts in the 'nice to have' area of the brief I am very interested to see how you guys go, thank you for your designs so farĀ 

Target Market(s)

Builders, Developers, Home Owners, Buissness Owners

Industry/Entity Type

Plastic

Requirements
Must have
• The Logo "Vorplex" which is attached to the project
(m)0412 557 163
(e)sales@vorplex.com.au

I would like the side Logo on the van to run diagonal & hopefully take most of the advertising space over the sliding door & rear panel

REC No: 48302
Nice to have
• I have spent a little extra money on the Vans with more to come and I believe they look sharp & clean with the view to target well to do clients & larger projects, it would be great to keep the vans looking professional & clean. I like blue, white, black, lime-pale green against the silver colour but open to surjection.
In my head I imagined the Vorplex logo running on the largest side panels on the diagonal with the Electrical, Security, AV also running the length underneath the logo. With some of the words mentioned above that describe our services in various shades randomly placed horizontally in the back ground linked together with a sort of printed circuit board pattern. Again I am very open to ideas so please feel free to get creative. You can see one image I have uploaded a picture of a Ute with some words that are randomly placed & similar to the shade I am thinking of, I also like the Lime/Pale Green on the Ute if you can make it work
Measurements of Van Panels are attached

```html
<!DOCTYPE html>
<html lang="en">
<head>
<meta charset="utf-8">
<title>Vorplex Van Wrap Layout</title>
<link rel="stylesheet" href="https://fonts.googleapis.com/css2?family=Arimo:wght@400&family=Cormorant+SC:wght@500&display=swap">
<style>
  :root{
    --canvas:#ffffff;
    --body-white:#ffffff;
    --outline:#1a1a1a;
    --glass:#5f6062;
    --glass-dark:#1c1c1c;
    --trim:#5a5b5d;
    --tyre:#2a2a2a;
    --hub:#8a8b8d;
    --lime:#8cc63f;
    --front-green:#3bb44a;
    --sky:#1ba1e2;
    --wrap-blue:#22a7e8;
    --logo-grey:#6f6a66;
    --tail-red:#d8262c;
    --lamp-amber:#f6b91a;
  }
  html,body{margin:0;padding:0;overflow:hidden;background:var(--canvas);}
  .sheet{display:block;width:1200px;height:939px;}
  .word{font-family:"Arimo",Arial,sans-serif;}
  .word--blue{fill:var(--sky);}
  .word--green{fill:var(--lime);}
  .brand-name{font-family:"Arimo",Arial,sans-serif;fill:var(--logo-grey);}
  .tagline{font-family:"Cormorant SC",Georgia,serif;fill:var(--logo-grey);letter-spacing:1px;}
  .outline{stroke:var(--outline);stroke-width:3;stroke-linejoin:round;}
</style>
</head>
<body>
<svg class="sheet" viewBox="0 0 1200 939" xmlns="http://www.w3.org/2000/svg">

  <!-- SIDE VIEW -->
  <g class="van-side">
    <path class="outline" role="img" aria-label="Van body, side view"
      fill="var(--body-white)"
      d="M8 300 L22 230 Q40 185 120 160 L230 120 Q300 40 340 30 L1110 10 Q1150 10 1160 60 L1170 300 L1190 320 L1190 350 L1150 355 L860 360 L300 360 L20 350 Z"/>
    <path fill="var(--glass)" class="outline" d="M290 130 L330 48 L480 44 L480 150 L290 155 Z"/>
    <rect fill="var(--glass)" x="525" y="33" width="142" height="128" rx="8"/>
    <rect fill="var(--glass-dark)" x="525" y="115" width="142" height="46"/>
    <rect fill="var(--glass)" x="687" y="33" width="117" height="128" rx="8"/>
    <rect fill="var(--glass-dark)" x="687" y="115" width="117" height="46"/>
    <rect fill="var(--glass-dark)" x="822" y="28" width="298" height="127" rx="14"/>
    <rect fill="var(--tail-red)" x="1125" y="60" width="40" height="150" rx="6"/>
    <rect fill="var(--lamp-amber)" x="26" y="232" width="54" height="58" rx="4"/>
    <rect fill="var(--trim)" x="5" y="300" width="115" height="45" rx="8"/>
    <rect fill="var(--trim)" x="1150" y="310" width="48" height="42" rx="6"/>
    <line x1="300" y1="338" x2="840" y2="333" stroke="var(--lime)" stroke-width="4"/>
    <line x1="505" y1="20" x2="505" y2="355" stroke="var(--outline)" stroke-width="2"/>
    <line x1="680" y1="20" x2="680" y2="355" stroke="var(--outline)" stroke-width="2"/>
    <line x1="815" y1="18" x2="815" y2="355" stroke="var(--outline)" stroke-width="2"/>
    <circle cx="215" cy="365" r="85" fill="var(--tyre)"/>
    <circle cx="215" cy="365" r="48" fill="var(--hub)"/>
    <circle cx="945" cy="365" r="85" fill="var(--tyre)"/>
    <circle cx="945" cy="365" r="48" fill="var(--hub)"/>

    <text class="word word--blue" x="835" y="90" font-size="34">0412 557 163</text>
    <text class="word word--green" x="840" y="126" font-size="21">sales@vorplex.com.au</text>
    <text class="word word--blue" x="882" y="174" font-size="18">Audio Visual</text>
    <circle cx="886" cy="200" r="12" fill="var(--lime)" stroke="var(--outline)" stroke-width="1"/>
    <text class="word word--blue" x="822" y="236" font-size="18">Surround Sound</text>
    <text class="word word--green" x="972" y="213" font-size="36">Electrical</text>
    <text class="word word--blue" x="1052" y="250" font-size="22">Security</text>

    <text class="word word--green" x="95" y="228" font-size="22">AV</text>
    <text class="word word--blue" x="148" y="205" font-size="20">Data</text>
    <text class="word word--green" x="232" y="200" font-size="23">Access Control</text>
    <text class="word word--blue" x="190" y="240" font-size="23">Automation</text>
    <text class="word word--blue" x="364" y="243" font-size="31">Alarms</text>
    <text class="word word--green" x="322" y="300" font-size="24">Networking</text>

    <text class="brand-name" x="512" y="285" font-size="92">Vorplex</text>
    <text class="tagline" x="541" y="304" font-size="14">Electrical, Security, AV</text>
  </g>

  <!-- FRONT VIEW -->
  <g class="van-front">
    <path class="outline" role="img" aria-label="Van body, front view"
      fill="var(--front-green)"
      d="M130 700 L150 560 Q160 522 200 520 L490 520 Q530 522 540 560 L560 700 L585 720 L585 900 L105 900 L105 720 Z"/>
    <path fill="#eeeeee" class="outline" d="M160 640 L170 545 L520 545 L530 640 Z"/>
    <rect fill="var(--wrap-blue)" x="78" y="598" width="40" height="52" rx="6"/>
    <rect fill="var(--wrap-blue)" x="532" y="598" width="40" height="52" rx="6"/>
    <rect fill="var(--body-white)" x="262" y="660" width="148" height="58" stroke="#cccccc"/>
    <text class="brand-name" x="272" y="702" font-size="32">Vorplex</text>
    <text class="tagline" x="282" y="713" font-size="7">Electrical, Security, AV</text>
    <rect fill="var(--lamp-amber)" x="118" y="722" width="82" height="72" rx="6"/>
    <rect fill="var(--lamp-amber)" x="470" y="722" width="82" height="72" rx="6"/>
    <rect fill="var(--trim)" x="205" y="728" width="262" height="80" rx="4"/>
    <rect fill="var(--trim)" x="105" y="810" width="480" height="70" rx="10"/>
    <rect fill="var(--body-white)" x="282" y="845" width="110" height="42" stroke="var(--outline)"/>
    <rect fill="var(--tyre)" x="122" y="880" width="60" height="55"/>
    <rect fill="var(--tyre)" x="490" y="880" width="60" height="55"/>
  </g>

  <!-- REAR VIEW -->
  <g class="van-rear">
    <path class="outline" role="img" aria-label="Van body, rear view"
      fill="var(--wrap-blue)"
      d="M640 600 Q650 525 700 518 L1000 518 Q1050 525 1060 600 L1062 860 L638 860 Z"/>
    <rect fill="var(--body-white)" x="670" y="670" width="362" height="190"/>
    <rect fill="var(--body-white)" x="670" y="525" width="362" height="145"/>
    <rect fill="var(--glass)" x="682" y="535" width="158" height="130" rx="10"/>
    <rect fill="var(--glass-dark)" x="682" y="610" width="158" height="55"/>
    <rect fill="var(--glass)" x="862" y="535" width="158" height="130" rx="10"/>
    <rect fill="var(--glass-dark)" x="862" y="610" width="158" height="55"/>
    <rect fill="var(--tail-red)" x="645" y="595" width="25" height="110" rx="4"/>
    <rect fill="var(--tail-red)" x="1032" y="595" width="25" height="110" rx="4"/>
    <line x1="851" y1="525" x2="851" y2="860" stroke="var(--outline)" stroke-width="2"/>
    <rect fill="var(--trim)" x="625" y="855" width="450" height="50" rx="8"/>
    <rect fill="var(--tyre)" x="650" y="900" width="60" height="36"/>
    <rect fill="var(--tyre)" x="995" y="900" width="60" height="36"/>

    <text class="word word--blue" x="703" y="641" font-size="17">0412 557 163</text>
    <text class="word word--green" x="868" y="638" font-size="13">sales@vorplex.com.au</text>
    <text class="word word--green" x="690" y="693" font-size="18">Domestic</text>
    <text class="word word--blue" x="912" y="693" font-size="20">Commercial</text>
    <text class="brand-name" x="705" y="788" font-size="88">Vorplex</text>
    <text class="tagline" x="718" y="790" font-size="1" opacity="0"> </text>
    <text class="tagline" x="716" y="790" font-size="13" dy="0"></text>
    <text class="tagline" x="716" y="802" font-size="13">Electrical, Security, AV</text>
    <text class="word word--blue" x="679" y="816" font-size="18">0412 557 163</text>
    <text class="word word--green" x="862" y="816" font-size="15">sales@vorplex.com.au</text>
  </g>
</svg>
</body>
</html>
```